Staywellon.com banner design

Staywellon.com is looking for a designer to work with ongoing to create a variety of banners.

For this competition we are looking for entrants to create two flash banners with dimensions 300x250 and a static banner/jpg. Each flash banner has two separate concepts one with more copy and more required 'slides' and one with less. The copy for each banner is as follows:

Concept 1: - 4 slide flash banner/animated gif
Save up to 75% on 150,000 Hotels Worldwide.
10% of profits go to local charities.
Do something good when you travel.
End screen call to action - Book now @ staywellon.com (click here)

Concept 1a: 3 slide flash banner/animated gif

Concept 2: 4 slide flash banner/animated gif
$0 Booking fees. Best price guarantee.

Concept 2a: 3 slide flash banner/animated gif

Concept 3 – Static Banner
Book now @ staywellon.com (click here)

Concept 3a

We expect two different designs, one for Concept 1 and 1a and a different design for concept 2 and 2a. Concept 3 (the static banners) can adopt the design used for the flash banners.

We also expect a gif version of the flash banners to be delivered.

The winning entry will then be hired to create each banner in a variety of banner sizes.

Reason: We are not satisfied with the number of entries so are extending this competition. We are looking for a long term relationship with a quality designer to produce a whole range of banners and other designs for staywellon.com.

Requirements
Must have
• The staywellon.com logo must always be visible on all banners.

Maximum flash file size is 50k
Max Frame Rate 24fps

```html
<!DOCTYPE html>
<html lang="en">
<head>
<meta charset="utf-8">
<title>Staywellon.com banner set</title>
<link href="https://fonts.googleapis.com/css2?family=Arimo:wght@400;700&display=swap" rel="stylesheet">
<style>
  :root {
    --page: #ffffff;
    --frame-orange: #f7931e;
    --label-grey: #9a9a9a;
    --sky-top: #2386d6;
    --sky-bottom: #0b5aa8;
    --border-grey: #b9b9b9;
    --white: #ffffff;
    --orange-hot: #fba026;
    --orange-deep: #f07f12;
    --gold: #ffd24a;
    --ice: #d8f0ff;
    --brown: #6b2a0a;
    --brown-text: #7a2e08;
    --ink: #333333;
    --tag-black: #1a1a1a;
    --tag-green: #1aa23a;
    --tag-blue: #8cc8f0;
    --photo-sky: #5f9fd8;
    --photo-green: #4f8a3c;
    --photo-stone: #c9c4b8;
  }
  * { box-sizing: border-box; margin: 0; padding: 0; }
  html, body {
    width: 1200px; height: 1200px; overflow: hidden;
    background: var(--page);
    font-family: "Arimo", Arial, sans-serif;
  }
  .sheet {
    position: relative; width: 800px; height: 800px;
    transform: scale(1.5); transform-origin: 0 0;
  }
  .animated-group {
    position: absolute; left: 56px; top: 6px; width: 688px; height: 525px;
    border: 3px solid var(--frame-orange);
  }
  .slide-label {
    position: absolute; font-size: 26px; color: var(--label-grey); font-weight: 400;
  }
  .group-caption {
    position: absolute; color: var(--frame-orange); font-size: 21px; text-align: center; line-height: 28px;
  }
  .banner {
    position: absolute; width: 300px; height: 250px; overflow: hidden;
    border: 1px solid var(--border-grey); background: var(--white);
  }
  .banner-sky {
    position: absolute; left: 0; top: 0; width: 100%; height: 215px;
    background: linear-gradient(160deg, var(--sky-top) 0%, var(--sky-bottom) 100%);
  }
  .banner-footer {
    position: absolute; left: 0; top: 215px; width: 100%; height: 35px;
    display: flex; align-items: center; justify-content: center; gap: 6px;
    background: var(--white);
  }
  .brand-dot { width: 18px; height: 18px; border-radius: 50%; background: var(--orange-deep); }
  .brand-name { font-size: 17px; font-weight: 700; color: var(--ink); letter-spacing: -0.2px; }
  .photo {
    position: absolute; background: var(--white); padding: 5px;
    box-shadow: 1px 2px 4px rgba(0,0,0,0.4);
  }
  .photo-fill { width: 100%; height: 100%; }
  .photo-dome .photo-fill { background: linear-gradient(170deg, var(--photo-sky) 0%, var(--photo-stone) 75%); }
  .photo-pool .photo-fill { background: linear-gradient(180deg, var(--photo-stone) 0%, var(--photo-green) 55%, var(--photo-sky) 100%); }
  .photo-balcony .photo-fill { background: linear-gradient(180deg, #e8e6e0 0%, var(--photo-stone) 60%, var(--photo-sky) 100%); }
  .cta {
    position: absolute; left: 70px; width: 155px; height: 40px; border-radius: 6px;
    background: linear-gradient(180deg, var(--orange-hot) 0%, var(--orange-deep) 100%);
    box-shadow: 0 2px 3px rgba(0,0,0,0.35);
    display: flex; align-items: center; justify-content: center; gap: 9px;
    font-size: 17px; font-weight: 700; color: var(--brown-text);
  }
  .cta-arrow {
    width: 26px; height: 24px; border-radius: 3px; background: var(--brown);
    display: flex; align-items: center; justify-content: center;
  }
  .headline { position: absolute; font-weight: 700; color: var(--white); line-height: 1; }
  .big-figure { color: var(--orange-hot); font-size: 46px; letter-spacing: -1px; }
  .tag {
    position: absolute; font-size: 12.5px; font-weight: 700; color: var(--white);
    display: flex; align-items: center; padding-left: 6px; line-height: 13px;
  }
  .tag-mark { width: 0; height: 0; border-left: 6px solid var(--white); border-top: 4px solid transparent; border-bottom: 4px solid transparent; margin-right: 5px; flex: none; }
</style>
</head>
<body>
<main class="sheet">

  <section class="animated-group" aria-label="Animated GIF slides"></section>
  <span class="slide-label" style="left:66px;top:120px;">A</span>
  <span class="slide-label" style="left:712px;top:120px;">B</span>
  <span class="slide-label" style="left:66px;top:357px;">C</span>
  <span class="slide-label" style="left:712px;top:357px;">D</span>
  <p class="group-caption" style="left:640px;top:536px;width:106px;">Animated<br>Gif</p>
  <p class="group-caption" style="left:90px;top:630px;width:130px;font-size:24px;line-height:34px;">Static<br>300X250</p>

  <!-- Slide A -->
  <article class="banner" style="left:95px;top:14px;">
    <div class="banner-sky"></div>
    <div class="headline" style="left:48px;top:8px;font-size:17px;">SAVE UP TO</div>
    <div class="headline big-figure" style="left:168px;top:6px;">75%</div>
    <div class="headline" style="left:48px;top:28px;font-size:17px;">ON 150,000</div>
    <div class="headline" style="left:48px;top:48px;font-size:12.5px;">HOTELS WORLDWIDE</div>
    <div class="photo photo-dome" style="left:8px;top:78px;width:94px;height:112px;transform:rotate(-6deg);"><div class="photo-fill" role="img" aria-label="Photo of a domed glass hotel building"></div></div>
    <div class="photo photo-pool" style="left:105px;top:74px;width:88px;height:108px;"><div class="photo-fill" role="img" aria-label="Photo of a resort hotel with palms and pool"></div></div>
    <div class="photo photo-balcony" style="left:196px;top:80px;width:92px;height:112px;transform:rotate(8deg);"><div class="photo-fill" role="img" aria-label="Photo of hotel balconies above a pool"></div></div>
    <div class="cta" style="top:167px;">CLICK HERE <span class="cta-arrow"><svg width="10" height="12" viewBox="0 0 10 12"><path d="M1 0 L10 6 L1 12 Z" fill="#ffffff"/></svg></span></div>
    <footer class="banner-footer"><span class="brand-dot"></span><span class="brand-name">Staywellon.com</span></footer>
  </article>

  <!-- Slide B -->
  <article class="banner" style="left:408px;top:14px;">
    <div class="banner-sky"></div>
    <div class="headline big-figure" style="left:30px;top:12px;">10%</div>
    <div class="headline" style="left:128px;top:14px;font-size:17px;line-height:20px;">of Profits Go to<br>Local Charities</div>
    <div class="photo photo-dome" style="left:8px;top:78px;width:94px;height:112px;transform:rotate(-6deg);"><div class="photo-fill" role="img" aria-label="Photo of a domed glass hotel building"></div></div>
    <div class="photo photo-pool" style="left:105px;top:74px;width:88px;height:108px;"><div class="photo-fill" role="img" aria-label="Photo of a resort hotel with palms and pool"></div></div>
    <div class="photo photo-balcony" style="left:196px;top:80px;width:92px;height:112px;transform:rotate(8deg);"><div class="photo-fill" role="img" aria-label="Photo of hotel balconies above a pool"></div></div>
    <div class="cta" style="top:167px;">CLICK HERE <span class="cta-arrow"><svg width="10" height="12" viewBox="0 0 10 12"><path d="M1 0 L10 6 L1 12 Z" fill="#ffffff"/></svg></span></div>
    <footer class="banner-footer"><span class="brand-dot"></span><span class="brand-name">Staywellon.com</span></footer>
  </article>

  <!-- Slide C -->
  <article class="banner" style="left:95px;top:270px;">
    <div class="banner-sky"></div>
    <div class="headline" style="left:0;top:9px;width:100%;text-align:center;font-size:21px;line-height:28px;color:var(--gold);">Do Something Good<br>When You Travel</div>
    <div class="photo photo-dome" style="left:8px;top:78px;width:94px;height:112px;transform:rotate(-6deg);"><div class="photo-fill" role="img" aria-label="Photo of a domed glass hotel building"></div></div>
    <div class="photo photo-pool" style="left:105px;top:74px;width:88px;height:108px;"><div class="photo-fill" role="img" aria-label="Photo of a resort hotel with palms and pool"></div></div>
    <div class="photo photo-balcony" style="left:196px;top:80px;width:92px;height:112px;transform:rotate(8deg);"><div class="photo-fill" role="img" aria-label="Photo of hotel balconies above a pool"></div></div>
    <div class="cta" style="top:167px;">CLICK HERE <span class="cta-arrow"><svg width="10" height="12" viewBox="0 0 10 12"><path d="M1 0 L10 6 L1 12 Z" fill="#ffffff"/></svg></span></div>
    <footer class="banner-footer"><span class="brand-dot"></span><span class="brand-name">Staywellon.com</span></footer>
  </article>

  <!-- Slide D -->
  <article class="banner" style="left:408px;top:270px;">
    <div class="banner-sky"></div>
    <div class="headline" style="left:0;top:29px;width:100%;text-align:center;font-size:17px;color:var(--ice);">Book Now@staywellon.com</div>
    <div class="photo photo-dome" style="left:8px;top:78px;width:94px;height:112px;transform:rotate(-6deg);"><div class="photo-fill" role="img" aria-label="Photo of a domed glass hotel building"></div></div>
    <div class="photo photo-pool" style="left:105px;top:74px;width:88px;height:108px;"><div class="photo-fill" role="img" aria-label="Photo of a resort hotel with palms and pool"></div></div>
    <div class="photo photo-balcony" style="left:196px;top:80px;width:92px;height:112px;transform:rotate(8deg);"><div class="photo-fill" role="img" aria-label="Photo of hotel balconies above a pool"></div></div>
    <div class="cta" style="top:167px;">CLICK HERE <span class="cta-arrow"><svg width="10" height="12" viewBox="0 0 10 12"><path d="M1 0 L10 6 L1 12 Z" fill="#ffffff"/></svg></span></div>
    <footer class="banner-footer"><span class="brand-dot"></span><span class="brand-name">Staywellon.com</span></footer>
  </article>

  <!-- Static banner -->
  <article class="banner" style="left:242px;top:541px;">
    <div class="banner-sky"></div>
    <div class="tag" style="left:0;top:10px;width:216px;height:32px;background:var(--orange-deep);align-items:flex-start;padding-top:3px;">
      <span class="tag-mark" style="margin-top:3px;"></span><span style="text-align:center;width:190px;">Save up to 75% on 150,000<br>hotels worldwide</span>
    </div>
    <div class="tag" style="left:22px;top:46px;width:276px;height:23px;background:var(--tag-black);"><span class="tag-mark"></span>10% of profits go to local charities</div>
    <div class="tag" style="left:0;top:75px;width:272px;height:20px;background:var(--tag-green);"><span class="tag-mark"></span>Do Something Good when you travel</div>
    <div class="tag" style="left:55px;top:94px;width:243px;height:20px;background:var(--tag-blue);color:var(--ink);"><span class="tag-mark" style="border-left-color:var(--white);"></span>Book Now@staywellon.com</div>
    <div class="photo photo-dome" style="left:22px;top:126px;width:82px;height:90px;transform:rotate(-6deg);"><div class="photo-fill" role="img" aria-label="Photo of a domed glass hotel building"></div></div>
    <div class="photo photo-pool" style="left:108px;top:122px;width:76px;height:84px;"><div class="photo-fill" role="img" aria-label="Photo of a resort hotel with palms and pool"></div></div>
    <div class="photo photo-balcony" style="left:188px;top:128px;width:82px;height:90px;transform:rotate(8deg);"><div class="photo-fill" role="img" aria-label="Photo of hotel balconies above a pool"></div></div>
    <div class="cta" style="top:171px;">CLICK HERE <span class="cta-arrow"><svg width="10" height="12" viewBox="0 0 10 12"><path d="M1 0 L10 6 L1 12 Z" fill="#ffffff"/></svg></span></div>
    <footer class="banner-footer"><span class="brand-dot"></span><span class="brand-name">Staywellon.com</span></footer>
  </article>

</main>
</body>
</html>
```